TOR Global (Terrain Orchard and Resources) is a company positioning itself as a global leader in regenerative and sustainable agriculture and irrigation technologies and solutions, with a focus on soil health. Please read the attached information (which can be used in the website).
We're looking for a modern website which also compliments the agricultural sector and the natural resources we work with. We want the website to be fairly concise and to the point without elaborating too much. We would rather attract the clients to engage with us rather than drawing their own conclusions from the website.

```html
<!DOCTYPE html>
<html lang="en">
<head>
<meta charset="utf-8">
<title>TOR Global – Terrain Orchard and Resources</title>
<link href="https://fonts.googleapis.com/css2?family=Archivo:wght@400;500;600;700;800;900&family=Lato:wght@400;700&family=Arimo:wght@400;600;700&display=swap" rel="stylesheet">
<style>
:root{
  --olive:#8b9272;
  --blue:#47679a;
  --navy:#3b5a8c;
  --ink:#1d1d1d;
  --muted:#5e5e5e;
  --white:#ffffff;
  --soil:#2b211a;
  --footer:#141210;
}
*{margin:0;padding:0;box-sizing:border-box}
html,body{width:1200px;height:3484px;overflow:hidden;background:var(--white)}
body{position:relative;font-family:Arimo,Arial,sans-serif;color:var(--ink)}
.abs{position:absolute}
.topbar{left:0;top:0;width:1200px;height:40px;background:var(--olive)}
.topbar .welcome{left:317px;top:12px;font:700 14px Lato,sans-serif;color:var(--white);text-transform:uppercase}
.social-dots{right:112px;top:8px;display:flex;gap:8px}
.social-dots span{width:26px;height:26px;border-radius:50%;background:var(--white);opacity:.95}
.header{left:0;top:40px;width:1200px;height:85px;background:var(--white)}
.logo-disc{left:92px;top:-10px;width:190px;height:194px;border-radius:50%;background:var(--white);z-index:5}
.logo-name{left:112px;top:70px;z-index:6;font:800 30px Archivo,sans-serif;color:var(--blue);width:150px;text-align:center;line-height:1}
.contact-item{display:flex;align-items:center;gap:14px;font:400 15px Lato,sans-serif;color:var(--ink);line-height:1.5}
.ring{width:48px;height:48px;border-radius:50%;border:3px solid var(--olive);display:flex;align-items:center;justify-content:center;flex:none}
.nav{left:0;top:125px;width:1200px;height:58px;background:var(--blue)}
.nav ul{position:absolute;left:316px;top:24px;display:flex;gap:27px;list-style:none;font:700 16px Lato,sans-serif;color:var(--white)}
.nav li.active{text-decoration:underline}
.nav .cta{position:absolute;left:952px;top:0;width:136px;height:58px;background:var(--olive);color:var(--white);font:700 16px Lato,sans-serif;display:flex;align-items:center;justify-content:center}
.hero{left:0;top:183px;width:1200px;height:640px;background:radial-gradient(ellipse at 30% 40%,#6d8a3c 0%,#3c5a22 45%,#1e2e14 100%)}
.hero-hands{left:0;top:183px;width:560px;height:520px;background:radial-gradient(ellipse at 45% 55%,#c99a7d 0%,#a46f52 35%,rgba(60,40,20,0) 70%)}
.hero-title{left:600px;top:230px;font:900 64px/79px Archivo,sans-serif;color:var(--white);letter-spacing:.5px;width:590px}
.hero-sub{left:602px;top:478px;font:700 22px/36px Lato,sans-serif;color:var(--white);width:520px}
.btn{left:600px;top:556px;width:128px;height:47px;border-radius:6px;background:var(--white);color:var(--ink);font:700 16px Lato,sans-serif;display:flex;align-items:center;justify-content:center}
.h2{font:600 44px Archivo,sans-serif;color:var(--ink)}
.h2 em{font-style:normal;color:var(--blue)}
.leaf{display:inline-block;vertical-align:middle;margin-left:6px}
.mission-list{left:111px;top:950px;width:480px;list-style:none}
.mission-list li{position:relative;padding-left:35px;font:400 13.5px/24px Arimo,sans-serif;color:var(--muted);margin-bottom:13px}
.mission-list li::before{content:"";position:absolute;left:0;top:4px;width:19px;height:19px;border-radius:50%;background:var(--olive)}
.mission-art{left:665px;top:790px;width:350px;height:390px;border-radius:50%;background:radial-gradient(circle at 50% 55%,#7b8f3e 0%,#6a4a30 45%,#3c2a1d 100%)}
.soil{left:0;top:1190px;width:1200px;height:820px;background:radial-gradient(ellipse at 50% 40%,#5a4634 0%,#3a2c20 50%,#241a13 100%)}
.services-title{left:0;top:1340px;width:1200px;text-align:center;font:600 44px Archivo,sans-serif;color:var(--white)}
.card{width:285px;background:var(--white);border-radius:0 0 40px 0;border:8px solid var(--white);box-shadow:6px 6px 0 var(--olive);overflow:hidden}
.card .photo{height:228px;border-radius:0 0 40px 0}
.card h3{font:700 17px/24px Arimo,sans-serif;color:var(--ink);padding:14px 4px 4px 5px}
.card p{font:400 12.5px/24px Arimo,sans-serif;color:var(--muted);padding:0 5px 14px}
.why-item{display:flex;gap:20px;width:460px}
.why-item .badge{width:80px;height:80px;border-radius:50%;border:7px solid var(--olive);background:var(--white);flex:none;display:flex;align-items:center;justify-content:center}
.why-item .badge.blue{border-color:var(--blue)}
.why-item .badge i{width:34px;height:34px;border:2.5px solid var(--blue);border-radius:50%}
.why-item h4{font:600 18px Arimo,sans-serif;color:var(--ink);margin-top:10px}
.why-item p{font:400 13.5px/24px Arimo,sans-serif;color:var(--muted);margin-top:2px}
.impact{left:111px;top:2618px;width:977px;height:280px;border-radius:140px;background:linear-gradient(90deg,#4a3322 0%,#2a1e16 40%,#141210 100%);overflow:hidden}
.impact h2{left:382px;top:60px;font:600 44px Archivo,sans-serif;color:var(--white)}
.impact p{left:382px;top:130px;width:540px;font:700 15px/31px Arimo,sans-serif;color:var(--white)}
.footer{left:0;top:3000px;width:1200px;height:484px;background:linear-gradient(180deg,#2a2520 0%,var(--footer) 60%)}
.foot-col h5{font:600 22px Arimo,sans-serif;color:var(--white);margin-bottom:14px}
.foot-col li{list-style:none;font:400 15.5px/28px Arimo,sans-serif;color:var(--white)}
.foot-contact li{display:flex;align-items:center;gap:12px;margin-bottom:25px}
.foot-contact li i,.foot-social li i{width:26px;height:26px;border-radius:50%;background:var(--white);flex:none}
.foot-social li{display:flex;align-items:center;gap:16px;margin-bottom:16px}
.foot-social li i{width:22px;height:22px;background:#e9e9e9}
.divider{left:111px;top:3445px;width:977px;height:1px;background:#777}
.copy{left:0;top:3456px;width:1200px;text-align:center;font:400 12px Arimo,sans-serif;color:var(--white)}
</style>
</head>
<body>

<div class="abs topbar">
  <div class="abs welcome">Welcome to Terrain Orchard &amp; Resources</div>
  <div class="abs social-dots"><span></span><span></span><span></span><span></span><span></span></div>
</div>

<header class="abs header">
  <div class="abs contact-item" style="left:460px;top:20px">
    <div class="ring"><svg width="20" height="24" viewBox="0 0 20 24"><path d="M10 1a8 8 0 0 1 8 8c0 6-8 14-8 14S2 15 2 9a8 8 0 0 1 8-8z" fill="none" stroke="#47679a" stroke-width="2.5"/><circle cx="10" cy="9" r="3" fill="#47679a"/></svg></div>
    <div>Lorem Ipsum,<br>USA- 437916</div>
  </div>
  <div class="abs contact-item" style="left:678px;top:20px">
    <div class="ring"><svg width="22" height="22" viewBox="0 0 24 24"><path d="M6 2l4 5-2 3c1 3 3 5 6 6l3-2 5 4-2 4C10 22 2 14 2 4z" fill="#47679a"/></svg></div>
    <div>+1 555 010 2468</div>
  </div>
  <div class="abs contact-item" style="left:896px;top:20px">
    <div class="ring"><svg width="22" height="16" viewBox="0 0 22 16"><rect x="1" y="1" width="20" height="14" rx="2" fill="#47679a"/><path d="M2 2l9 7 9-7" fill="none" stroke="#fff" stroke-width="1.6"/></svg></div>
    <div>hello@torglobal.net</div>
  </div>
</header>

<nav class="abs nav">
  <ul>
    <li class="active">Home</li><li>About Us</li><li>Services</li><li>Why Choose Us</li><li>Impact</li><li>Testimonials</li>
  </ul>
  <div class="cta">Contact Us</div>
</nav>

<div class="abs logo-disc"></div>
<div class="abs logo-name">TOR Global</div>

<section>
  <div class="abs hero" role="img" aria-label="Green blurred field background"></div>
  <div class="abs hero-hands" role="img" aria-label="Cupped hands holding soil with a young seedling"></div>
  <h1 class="abs hero-title">Terrain Orchard and Resources (TOR)</h1>
  <p class="abs hero-sub">Revolutionizing Agriculture with Regenerative Solutions</p>
  <div class="abs btn">Get Started</div>
  <svg class="abs" style="left:0;top:660px" width="1200" height="170" viewBox="0 0 1200 170">
    <path d="M0 20 C250 140 380 150 560 110 C760 60 950 -10 1200 80 L1200 170 L0 170Z" fill="#fff"/>
    <path d="M0 20 C200 130 330 170 520 150 C740 120 900 30 1200 90" fill="none" stroke="#3b5a8c" stroke-width="14"/>
  </svg>
</section>

<section>
  <h2 class="abs h2" style="left:111px;top:878px">Our <em>Mission</em><svg class="leaf" width="28" height="28" viewBox="0 0 28 28"><path d="M3 25C3 10 13 3 26 3c0 14-8 22-23 22z" fill="#8b9272"/><path d="M5 23L20 9" stroke="#fff" stroke-width="2"/></svg></h2>
  <ul class="abs mission-list">
    <li>At TOR, we are committed to reshaping the future of farming through regenerative agriculture.</li>
    <li>Our solutions go beyond sustainability, actively restoring ecosystems and improving soil health while delivering superior yields.</li>
    <li>With water-efficient irrigation, innovative agronomy, and a deep focus on soil vitality, we empower farmers to grow more sustainably and profitably.</li>
  </ul>
  <div class="abs mission-art" role="img" aria-label="Globe and gear illustration filled with soil and a sprouting plant"></div>
</section>

<section>
  <div class="abs soil" role="img" aria-label="Dark soil with hands planting crops"></div>
  <svg class="abs" style="left:0;top:1188px" width="1200" height="100" viewBox="0 0 1200 100"><path d="M0 0 L1200 0 L1200 5 C1000 -5 850 70 560 90 C300 105 150 60 0 10Z" fill="#fff"/></svg>
  <svg class="abs" style="left:0;top:1930px" width="1200" height="82" viewBox="0 0 1200 82"><path d="M0 20 C250 35 450 0 650 5 C900 10 1050 70 1200 80 L1200 82 L0 82Z" fill="#fff"/></svg>
  <h2 class="abs services-title">Our Core Products and Services<svg class="leaf" width="30" height="30" viewBox="0 0 28 28"><path d="M3 25C3 10 13 3 26 3c0 14-8 22-23 22z" fill="#fff"/><path d="M5 23L20 9" stroke="#3a2c20" stroke-width="2"/></svg></h2>

  <div class="abs card" style="left:11px;top:1432px">
    <div class="photo" role="img" aria-label="Farmers inspecting crops beside a solar panel" style="background:linear-gradient(160deg,#c9d6e0,#7f8f5a 60%,#5a6a3a)"></div>
    <h3>Regenerative Agricultural Technologies</h3>
    <p>Unlock the future of farming with the latest practices and tools designed to rebuild ecosystems, improve biodiversity, and restore soil carbon levels.</p>
  </div>
  <div class="abs card" style="left:307px;top:1478px">
    <h3 style="padding-top:20px">Mobile Drip Irrigation (MDI)</h3>
    <p>Our advanced irrigation system maximizes water use efficiency, reduces waste, and promotes healthier crops.</p>
    <div class="photo" role="img" aria-label="Hand holding a phone over rows of irrigated seedlings" style="background:linear-gradient(160deg,#5f8a3a,#3a6a8a 55%,#2a4a2a)"></div>
  </div>
  <div class="abs card" style="left:608px;top:1432px">
    <div class="photo" role="img" aria-label="Farmer operating a small soil tiller" style="background:linear-gradient(160deg,#a89a88,#6d5a48 60%,#4a3a2e)"></div>
    <h3>Agronomy Services</h3>
    <p>Expert advice and customized crop management plans to boost productivity while supporting regenerative outcomes.</p>
  </div>
  <div class="abs card" style="left:903px;top:1478px">
    <h3 style="padding-top:20px">Soil Health Solutions</h3>
    <p>From analysis to rehabilitation, we help you restore soil fertility, improve water retention, and reduce dependency on chemical inputs.</p>
    <div class="photo" role="img" aria-label="Potted plants with soil sample tubes" style="background:linear-gradient(160deg,#8aa84a,#b46a52 55%,#6a4a3a)"></div>
  </div>
</section>

<section>
  <h2 class="abs h2" style="left:111px;top:2034px;font-weight:400">Why <em style="font-weight:600">Choose TOR?</em><svg class="leaf" width="28" height="28" viewBox="0 0 28 28"><path d="M3 25C3 10 13 3 26 3c0 14-8 22-23 22z" fill="#8b9272"/><path d="M5 23L20 9" stroke="#fff" stroke-width="2"/></svg></h2>
  <div class="abs why-item" style="left:111px;top:2140px"><div class="badge"><i></i></div><div><h4>Champions of Regenerative Agriculture:</h4><p>We don't just sustain—we regenerate, creating long-term benefits for the environment and your farm.</p></div></div>
  <div class="abs why-item" style="left:111px;top:2245px"><div class="badge blue"><i></i></div><div><h4>Cutting-Edge Innovation:</h4><p>Access the latest technologies that promote ecosystem restoration and climate resilience.</p></div></div>
  <div class="abs why-item" style="left:111px;top:2351px"><div class="badge"><i></i></div><div><h4>Global Expertise:</h4><p>Decades of experience bringing sustainable solutions to diverse farming environments worldwide.</p></div></div>
  <div class="abs why-item" style="left:111px;top:2456px"><div class="badge blue"><i></i></div><div><h4>Tailored for Your Success:</h4><p>We work with you to create strategies that meet the unique needs of your farm and community.</p></div></div>
  <div class="abs" role="img" aria-label="Leaf-shaped frame with hands holding a glowing seedling" style="left:630px;top:2102px;width:415px;height:418px;background:radial-gradient(circle at 55% 45%,#3fa040 0%,#2a4a5a 40%,#1a2230 80%);clip-path:path('M415 0 C420 200 330 400 90 418 C-20 300 0 120 415 0Z')"></div>
</section>

<section>
  <div class="abs impact" role="img" aria-label="Young corn seedling growing from dark soil">
    <h2 class="abs">Our Impact<svg class="leaf" width="30" height="30" viewBox="0 0 28 28"><path d="M3 25C3 10 13 3 26 3c0 14-8 22-23 22z" fill="#fff"/><path d="M5 23L20 9" stroke="#222" stroke-width="2"/></svg></h2>
    <p class="abs">We are proud to help farmers build resilient farms, sequester carbon, and regenerate the land. Our approach ensures healthy soils, vibrant ecosystems, and productive crops for generations to come.</p>
  </div>
</section>

<footer>
  <div class="abs footer" role="img" aria-label="Dark field background"></div>
  <svg class="abs" style="left:0;top:2975px" width="1200" height="150" viewBox="0 0 1200 150">
    <path d="M0 0 L1200 0 L1200 110 C1000 -20 800 10 600 70 C400 130 200 130 0 40Z" fill="#fff"/>
    <path d="M0 40 C200 140 400 120 600 70 C800 15 1000 -10 1200 115" fill="none" stroke="#3b5a8c" stroke-width="14"/>
  </svg>
  <div class="abs" style="left:800px;top:3080px;font:800 34px Archivo,sans-serif;color:#fff">TOR Global</div>
  <div class="abs foot-col" style="left:118px;top:3188px"><h5>Quick Links</h5><ul><li>Home</li><li>About Us</li><li>Services</li><li>Why Choose Us</li><li>Impact</li><li>Testimonials</li><li>Contact Us</li></ul></div>
  <div class="abs foot-col" style="left:358px;top:3188px"><h5>Help Links</h5><ul><li>Privacy Policy</li><li>Terms &amp; Conditions</li><li>Disclaimer</li></ul></div>
  <div class="abs foot-col foot-contact" style="left:604px;top:3184px"><h5>Contact Info</h5><ul><li><i></i>Lorem Ipsum,USA - 437916</li><li><i></i>+1 555 010 24680</li><li><i></i>hello@torglobal.net</li></ul></div>
  <div class="abs foot-col foot-social" style="left:906px;top:3184px"><h5>Follow Us</h5><ul><li><i></i>Fieldbook</li><li><i></i>Chirper</li><li><i></i>Snapgram</li><li><i></i>Linkwork</li></ul></div>
  <div class="abs divider"></div>
  <div class="abs copy">Copyright © 2024 TOR Global. All rights reserved.</div>
</footer>

</body>
</html>
```